E-commerce Website needs category banner

What we need for our category banner is a clean, predominately black design that showcases the product we are trying to sell (currently only 1), and a few subtle gradients that follow the pattern set by previous designs.

An example will be provided to showcase what we want.

It needs to say:
Outdoor Motion Detection Lighting in large, clear font similar to the example provided.
Updates

Please ensure dimensions are as follows: 980x300

Target Market(s)

Senior citizens, businesses, homeowners, families, etc

Industry/Entity Type

Product

Font styles to use
Sans Serif

Requirements
Must have
• It needs to say:
Outdoor Motion Detection Lighting in large, clear font similar to the example provided
980x300 is the required size!
Should not have
• Too much going on- clean and simple please (no crazy fonts, logos, etc)

```html
<!DOCTYPE html>
<html lang="en">
<head>
<meta charset="utf-8">
<title>Category Banner – Outdoor Motion Detection Lighting</title>
<link rel="stylesheet" href="https://fonts.googleapis.com/css2?family=Barlow+Condensed:ital,wght@1,700&display=swap">
<style>
  :root {
    --board-center: #fbfbfb;
    --board-edge: #c4c4c4;
    --banner-glow: #313131;
    --banner-mid: #1a1a1a;
    --banner-edge: #050505;
    --headline-dim: #7a7a7a;
    --headline-bright: #ffffff;
    --product-light: #f4f4f4;
    --product-shade: #b9b9b9;
  }
  * { margin: 0; padding: 0; box-sizing: border-box; }
  html, body { width: 1200px; height: 1000px; overflow: hidden; }
  body {
    position: relative;
    background: radial-gradient(ellipse 70% 65% at 50% 50%, var(--board-center) 40%, var(--board-edge) 100%);
    font-family: "Barlow Condensed", "Arial Narrow", sans-serif;
  }
  .banner {
    position: absolute;
    container-type: inline-size;
    overflow: hidden;
    background: radial-gradient(ellipse 60% 70% at 58% 48%, var(--banner-glow) 0%, var(--banner-mid) 55%, var(--banner-edge) 100%);
  }
  .banner--main  { left: 96px;  top: 111px; width: 986px; height: 497px; }
  .banner--small-left  { left: 29px;  top: 658px; width: 560px; height: 282px; }
  .banner--small-right { left: 616px; top: 658px; width: 560px; height: 282px; }

  .product-shot {
    position: absolute;
    left: 6%;
    top: 27.5%;
    width: 18.3%;
    height: 44.5%;
    border-radius: 38% 30% 42% 36%;
    background: radial-gradient(ellipse at 35% 30%, var(--product-light) 0%, #dedede 50%, var(--product-shade) 100%);
  }
  .headline {
    position: absolute;
    left: 61.6%;
    top: 40%;
    transform: translateX(-50%);
    white-space: nowrap;
    text-align: center;
    font-style: italic;
    font-weight: 700;
    font-size: 4.85cqw;
    line-height: 1.0;
    letter-spacing: 0.07em;
    text-transform: uppercase;
    background: linear-gradient(90deg, var(--headline-dim) 0%, #b8b8b8 45%, var(--headline-bright) 70%);
    -webkit-background-clip: text;
    background-clip: text;
    color: transparent;
  }
</style>
</head>
<body>
  <section class="banner banner--main">
    <div class="product-shot" role="img" aria-label="White battery-powered outdoor motion sensor spotlight with two LEDs and wall mount"></div>
    <h1 class="headline">Outdoor Motion Detection<br>Lighting in Large</h1>
  </section>

  <section class="banner banner--small-left">
    <div class="product-shot" role="img" aria-label="White battery-powered outdoor motion sensor spotlight with two LEDs and wall mount"></div>
    <h2 class="headline">Outdoor Motion Detection<br>Lighting in Large</h2>
  </section>

  <section class="banner banner--small-right">
    <div class="product-shot" role="img" aria-label="White battery-powered outdoor motion sensor spotlight with two LEDs and wall mount"></div>
    <h2 class="headline">Outdoor Motion Detection<br>Lighting in Large</h2>
  </section>
</body>
</html>
```